Business Consultant need 4 page Eye Popping infographic type brochure

I am a business growth coach who operates in the visual communications industry.
I need for A4 size visuals that are clean looking, compelling and communicate clearly. The purpose is to visually explain how our new service works.
I’m looking for a clean style where the visuals pop off the page. Lots of white space.
The finished files must be ready by Monday, 13 February
If you are submitting sample work, you can do just one of the pages from those numbered 2 - 4.
I have provided hand drawn specs in the attached PDF - QNT5 Value Framework Hand Drawn Specs.
I have provided you with 10 different infographic samples that I like in this folder - Infographic Samples
I have also attached our general branding guidelines with the typical colour palette we work from in this PDF - Branding Guidelines
I need a supporting visual/logo for the name of each of the 4 services. We have a logo image for the 60-Day Climb (waiting on the final file) and I have provided samples for the other 3 in this folder - Logo Samples. You need to create the 3 missing logos.
We have a number of additional similar projects over the coming weeks and that means I’m looking for a great designer that I can form a long term relationship.
Looking forward to seeing your work
Reason: Working on the files
Target Market(s)
See attached branding guidelines
Industry/Entity Type
Business
Other font styles liked:
- See attached branding guidelines
Requirements
Must have
- See samples & branding guidelines
Nice to have
Should not have

```html
<!DOCTYPE html>
<html lang="en">
<head>
<meta charset="utf-8">
<title>Yield Plotting</title>
<link rel="stylesheet" href="https://fonts.googleapis.com/css2?family=Roboto:wght@400;500;900&family=Roboto+Condensed:wght@400;700&family=Montserrat:wght@800&display=swap">
<style>
  :root {
    --orange: #ef6b22;
    --orange-light: #f8b48c;
    --yellow: #fbb829;
    --yellow-light: #fde0a0;
    --green: #1e9a48;
    --green-light: #a6d8b4;
    --navy: #1f2c6b;
    --navy-light: #9aa0c6;
    --pink: #d81b5a;
    --red: #a5191f;
    --charcoal: #3b3b3d;
    --lime: #8cc63f;
    --brown: #7a4a3a;
    --band: #bfe4e4;
    --ink: #333335;
    --paper: #ffffff;
  }
  html, body {
    margin: 0;
    padding: 0;
    overflow: hidden;
    background: var(--paper);
  }
  .canvas {
    position: relative;
    width: 1200px;
    height: 857px;
    overflow: hidden;
    background: var(--paper);
    font-family: "Roboto", Arial, sans-serif;
    color: var(--ink);
  }
  .method-band {
    position: absolute;
    left: 0;
    top: 589px;
    width: 1200px;
    height: 268px;
    background: var(--band);
  }
  .brand-mark {
    position: absolute;
    left: 46px;
    top: 38px;
    width: 96px;
    height: 96px;
    border-radius: 50%;
    background: var(--orange);
  }
  .headline {
    position: absolute;
    left: 176px;
    top: 26px;
    margin: 0;
    font-size: 82px;
    line-height: 1;
    letter-spacing: -1px;
    white-space: nowrap;
  }
  .headline-light { color: var(--orange); font-weight: 400; }
  .headline-bold { color: var(--red); font-weight: 900; }
  .tagline {
    position: absolute;
    left: 180px;
    top: 116px;
    margin: 0;
    font-size: 17.5px;
    font-weight: 400;
    color: var(--ink);
    white-space: nowrap;
  }
  .artwork {
    position: absolute;
    left: 0;
    top: 0;
  }
  .ring-label { font-family: "Roboto Condensed", Arial, sans-serif; font-weight: 700; font-size: 25px; fill: #fff; letter-spacing: 1px; }
  .system-label { font-family: "Roboto Condensed", Arial, sans-serif; font-size: 22px; fill: var(--ink); letter-spacing: 1px; }
  .system-label .strong { font-weight: 700; }
  .stage-label { font-family: "Roboto Condensed", Arial, sans-serif; font-weight: 700; font-size: 19px; fill: var(--ink); }
  .lens-title { font-family: "Roboto Condensed", Arial, sans-serif; font-size: 27px; fill: var(--orange); }
  .lens-title .strong { font-weight: 700; }
  .lens-letter { font-family: "Montserrat", Arial, sans-serif; font-weight: 800; font-size: 72px; fill: var(--ink); text-anchor: middle; }
  .lens-word { font-family: "Roboto Condensed", Arial, sans-serif; font-size: 13px; fill: var(--ink); text-anchor: middle; }
  .method-title { font-family: "Roboto Condensed", Arial, sans-serif; font-size: 29px; fill: var(--orange); text-anchor: middle; }
  .method-title .strong { font-weight: 700; }
  .step-text { font-family: "Roboto Condensed", Arial, sans-serif; font-size: 15px; fill: #fff; text-anchor: middle; }
  .step-number { font-family: "Roboto", Arial, sans-serif; font-weight: 900; font-size: 26px; fill: var(--ink); text-anchor: middle; }
</style>
</head>
<body>
<main class="canvas">
  <div class="method-band"></div>

  <div class="brand-mark"></div>
  <h1 class="headline"><span class="headline-light">YIELD</span> <span class="headline-bold">PLOTTING</span></h1>
  <p class="tagline">Create continuous improvement that delivers IMPROVED FINANCIAL PERFORMANCE</p>

  <svg class="artwork" width="1200" height="857" viewBox="0 0 1200 857">
    <defs>
      <path id="arc-more" d="M123,382 A145,145 0 0 1 268,237"/>
      <path id="arc-better" d="M268,237 A145,145 0 0 1 413,382"/>
      <path id="arc-faster" d="M268,527 A145,145 0 0 0 413,382"/>
      <path id="arc-cheaper" d="M123,382 A145,145 0 0 0 268,527"/>
      <path id="arc-system" d="M70.7,453.8 A210,210 0 0 1 403,221"/>
      <marker id="cycle-head" viewBox="0 0 10 10" refX="5" refY="5" markerWidth="5" markerHeight="5" orient="auto">
        <path d="M0,0 L10,5 L0,10 Z" fill="var(--ink)"/>
      </marker>
    </defs>

    <g class="cycle">
      <text class="system-label"><textPath href="#arc-system">THE 5 STEP <tspan class="strong">YIELD PLOTTING SYSTEM</tspan></textPath></text>

      <use href="#arc-more" fill="none" stroke="var(--orange)" stroke-width="62"/>
      <use href="#arc-better" fill="none" stroke="var(--yellow)" stroke-width="62"/>
      <use href="#arc-faster" fill="none" stroke="var(--green)" stroke-width="62"/>
      <use href="#arc-cheaper" fill="none" stroke="var(--navy)" stroke-width="62"/>

      <text class="ring-label" dy="9"><textPath href="#arc-more" startOffset="50%" text-anchor="middle">MORE</textPath></text>
      <text class="ring-label" dy="9"><textPath href="#arc-better" startOffset="50%" text-anchor="middle">BETTER</textPath></text>
      <text class="ring-label" dy="9"><textPath href="#arc-faster" startOffset="50%" text-anchor="middle">FASTER</textPath></text>
      <text class="ring-label" dy="9"><textPath href="#arc-cheaper" startOffset="50%" text-anchor="middle">CHEAPER</textPath></text>

      <g class="cycle-node">
        <circle cx="268" cy="237" r="55" fill="var(--orange)"/>
        <circle cx="268" cy="237" r="43" fill="var(--orange-light)"/>
        <circle cx="268" cy="237" r="34" fill="#fff"/>
      </g>
      <g class="cycle-node">
        <circle cx="413" cy="382" r="55" fill="var(--yellow)"/>
        <circle cx="413" cy="382" r="43" fill="var(--yellow-light)"/>
        <circle cx="413" cy="382" r="34" fill="#fff"/>
      </g>
      <g class="cycle-node">
        <circle cx="268" cy="527" r="55" fill="var(--green)"/>
        <circle cx="268" cy="527" r="43" fill="var(--green-light)"/>
        <circle cx="268" cy="527" r="34" fill="#fff"/>
      </g>
      <g class="cycle-node">
        <circle cx="123" cy="382" r="55" fill="var(--navy)"/>
        <circle cx="123" cy="382" r="43" fill="var(--navy-light)"/>
        <circle cx="123" cy="382" r="34" fill="#fff"/>
      </g>

      <path d="M202.2,405.9 A70,70 0 1 1 333.8,405.9" fill="none" stroke="var(--ink)" stroke-width="2" marker-end="url(#cycle-head)"/>
    </g>

    <g class="timeline">
      <path d="M545,287 L1130,283 L1130,291 Z" fill="var(--red)"/>
      <circle cx="593" cy="287" r="9" fill="#fff" stroke="var(--orange)" stroke-width="4"/>
      <circle cx="712" cy="287" r="9" fill="#fff" stroke="var(--yellow)" stroke-width="4"/>
      <circle cx="833" cy="287" r="9" fill="#fff" stroke="var(--green)" stroke-width="4"/>
      <circle cx="953" cy="287" r="9" fill="#fff" stroke="var(--navy)" stroke-width="4"/>
      <circle cx="1072" cy="287" r="9" fill="#fff" stroke="var(--pink)" stroke-width="4"/>
      <text class="stage-label" x="593" y="242" text-anchor="middle">VISUALIZE IT</text>
      <text class="stage-label" x="712" y="338" text-anchor="middle">MEASURE IT</text>
      <text class="stage-label" x="833" y="246" text-anchor="middle">IMPROVE IT</text>
      <text class="stage-label" x="953" y="338" text-anchor="middle">RECREATE IT</text>
      <text class="stage-label" x="1072" y="246" text-anchor="middle">IMPLEMENT IT</text>
    </g>

    <g class="waste-lens">
      <text class="lens-title" x="530" y="414">THE <tspan class="strong">8 WAIST LENS</tspan></text>
      <path d="M800,418 H1155 Q1165,418 1165,428 V541 Q1165,551 1155,551 H529 Q519,551 519,541 V428" fill="none" stroke="var(--orange)" stroke-width="2"/>
      <text class="lens-letter" x="554" y="487">D</text>
      <text class="lens-letter" x="642" y="487">O</text>
      <text class="lens-letter" x="735" y="487">W</text>
      <text class="lens-letter" x="834" y="487">N</text>
      <text class="lens-letter" x="921" y="487">T</text>
      <text class="lens-letter" x="993" y="487">I</text>
      <text class="lens-letter" x="1042" y="487">M</text>
      <text class="lens-letter" x="1118" y="487">E</text>
      <text class="lens-word" x="551" y="512">Defects</text>
      <text class="lens-word" x="642" y="512">Over<tspan x="642" dy="15">Production</tspan></text>
      <text class="lens-word" x="737" y="512">Waiting</text>
      <text class="lens-word" x="834" y="512">Non<tspan x="834" dy="15">Utilized</tspan><tspan x="834" dy="15">Talent</tspan></text>
      <text class="lens-word" x="914" y="512">Transportation</text>
      <text class="lens-word" x="970" y="529">inventory</text>
      <text class="lens-word" x="1035" y="512">Motion</text>
      <text class="lens-word" x="1130" y="512">Extra<tspan x="1130" dy="15">Processing</tspan></text>
    </g>

    <g class="method">
      <text class="method-title" x="600" y="622">THE 7 STEP <tspan class="strong">SUMMIT METHOD</tspan></text>

      <g class="method-links" stroke-width="7" fill="none">
        <path d="M280,728 L315,742" stroke="var(--orange)"/>
        <path d="M397,742 L436,728" stroke="var(--yellow)"/>
        <path d="M527,728 L558,742" stroke="var(--green)"/>
        <path d="M643,742 L674,728" stroke="var(--navy)"/>
        <path d="M764,728 L799,742" stroke="var(--pink)"/>
        <path d="M883,742 L922,728" stroke="var(--red)"/>
        <path d="M1008,734 L1040,748" stroke="var(--brown)"/>
      </g>

      <g class="step" transform="translate(181,645)">
        <polygon points="0,0 109,0 109,116 54.5,104 0,116" fill="var(--orange)"/>
        <circle cx="54.5" cy="8" r="22" fill="#fff" stroke="var(--orange)" stroke-width="4"/>
        <text class="step-number" x="54.5" y="17">1</text>
        <text class="step-text" x="54.5" y="50">Agree<tspan x="54.5" dy="16">measurable</tspan><tspan x="54.5" dy="16">business</tspan><tspan x="54.5" dy="16">value</tspan></text>
      </g>
      <g class="step" transform="translate(304,705)">
        <polygon points="0,0 103,0 103,105 51.5,93 0,105" fill="var(--yellow)"/>
        <circle cx="51.5" cy="8" r="22" fill="#fff" stroke="var(--yellow)" stroke-width="4"/>
        <text class="step-number" x="51.5" y="17">2</text>
        <text class="step-text" x="51.5" y="48">Create a<tspan x="51.5" dy="16">product</tspan><tspan x="51.5" dy="16">backlog</tspan></text>
      </g>
      <g class="step" transform="translate(425,645)">
        <polygon points="0,0 112,0 112,109 56,97 0,109" fill="var(--green)"/>
        <circle cx="56" cy="8" r="22" fill="#fff" stroke="var(--green)" stroke-width="4"/>
        <text class="step-number" x="56" y="17">3</text>
        <text class="step-text" x="56" y="48">Estimate what<tspan x="56" dy="16">is possible</tspan><tspan x="56" dy="16">with</tspan><tspan x="56" dy="16">deliverables</tspan></text>
      </g>
      <g class="step" transform="translate(547,705)">
        <polygon points="0,0 106,0 106,105 53,93 0,105" fill="var(--navy)"/>
        <circle cx="53" cy="8" r="22" fill="#fff" stroke="var(--navy)" stroke-width="4"/>
        <text class="step-number" x="53" y="17">4</text>
        <text class="step-text" x="53" y="48">Prioritize<tspan x="53" dy="16">business</tspan><tspan x="53" dy="16">deliverables</tspan></text>
      </g>
      <g class="step" transform="translate(663,645)">
        <polygon points="0,0 111,0 111,109 55.5,97 0,109" fill="var(--pink)"/>
        <circle cx="55.5" cy="8" r="22" fill="#fff" stroke="var(--pink)" stroke-width="4"/>
        <text class="step-number" x="55.5" y="17">5</text>
        <text class="step-text" x="55.5" y="50">Execute<tspan x="55.5" dy="16">an sprint</tspan></text>
      </g>
      <g class="step" transform="translate(788,705)">
        <polygon points="0,0 105,0 105,105 52.5,93 0,105" fill="var(--red)"/>
        <circle cx="52.5" cy="8" r="22" fill="#fff" stroke="var(--red)" stroke-width="4"/>
        <text class="step-number" x="52.5" y="17">6</text>
        <text class="step-text" x="52.5" y="48">Make<tspan x="52.5" dy="16">it visible</tspan></text>
      </g>
      <g class="step" transform="translate(911,645)">
        <polygon points="0,0 107,0 107,116 53.5,104 0,116" fill="var(--charcoal)"/>
        <circle cx="53.5" cy="8" r="22" fill="#fff" stroke="var(--charcoal)" stroke-width="4"/>
        <text class="step-number" x="53.5" y="17">7</text>
        <text class="step-text" x="53.5" y="50">Review<tspan x="53.5" dy="16">learn</tspan><tspan x="53.5" dy="16">accept</tspan></text>
      </g>
      <g class="step-repeat">
        <polygon points="1030,698 1118,698 1144,747 1118,796 1030,796" fill="var(--lime)"/>
        <text class="step-text" x="1082" y="745">Repeat<tspan x="1082" dy="16">£ / $</tspan></text>
      </g>
    </g>
  </svg>
</main>
</body>
</html>
```